Re-design of our website - Property Development Company

Our current website is now old and stale. We are looking for a Wordpress design for a new website. Our company is a property development and property investment company. We have different projects that are under construction and have completed a number also. We would like to showcase these projects as individual pages. The projects are located all over the east coast of Australia and a mixture of retail, industrial, residential subdivsions. In the near future we are hoping to start a small property funds management division as well.

Current website is www.korvanith.com.au

We are wanting you to design a page for the each of following (total of 3 pages):
- Home page
- Project page (which will be used to showcase each development project). There are 4 active projects that we currently own and a number of completed projects.
- Information page (which will be used for about us, contact us, management etc.)

Feel free to go out of the box and wow us. We are open to new ideas.
Updates

Reason: Hi I am going on annual leave for a week being 17-21 Feb so wont be able to comment on anyones design so I have given you an extra week and a bit to finish off your 3 pages. Thanks for the designs so far, they are looking good.

Target Market(s)

It will be used by business professionals researching our company including:
- current investors
- new investors
- consultants (architects, builders, town planners, council, real estate managers/agents, engineers etc.)
- Bank lenders

We want these people to think yes we want to work with this company, they look like they are exceptional at what they do, professional, highly capable.

Industry/Entity Type

Investment

Requirements
Must have
• Our Logo. Files attached. This can be modified if you think it needs to be improved.
Nice to have
• We like clean looking websites.
• We will have some professional photographs taken of our current property developments once they are completed - two shopping centres that will be our signature developments to date. For the time being I have uploaded some aerial photographs on one of our projects under construction and also some nice photos of one of our completed developments. This should help with designing the project page.
Should not have
• We don't like busy websites with too much going on and you don't know what to look at.

```html
<!DOCTYPE html>
<html lang="en">
<head>
<meta charset="utf-8">
<title>Korvanith Partners</title>
<link href="https://fonts.googleapis.com/css2?family=Lato:wght@400;700&family=Ubuntu:wght@400;500;700&display=swap" rel="stylesheet">
<style>
:root{
  --blue:#1a73c4;
  --blue-dark:#0b5fae;
  --blue-light:#2f8fdd;
  --navy:#0e3f7a;
  --text:#666;
  --dark:#222;
  --darker:#191919;
  --yellow:#f1e66b;
  --white:#fff;
  --line:#e4e4e4;
}
*{margin:0;padding:0;box-sizing:border-box}
html,body{width:712px;height:1200px;overflow:hidden;background:var(--white)}
body{font-family:"Lato",sans-serif;color:var(--text);font-size:8px;line-height:1.55}
.page{position:relative;width:712px;height:1200px}

.site-header{height:68px;position:relative}
.brand{position:absolute;left:30px;top:20px;display:flex;align-items:center;gap:7px}
.brand-mark{width:22px;height:22px;background:var(--blue)}
.brand-name{font-size:17px;color:var(--blue);font-weight:700;line-height:1}
.social{position:absolute;right:42px;top:27px;display:flex;gap:7px}
.social span{width:12px;height:12px;background:var(--navy);border-radius:1px}

.main-nav{height:36px;background:linear-gradient(#1e86d6,#0a62b4);display:flex;align-items:stretch;padding-left:30px;position:relative}
.main-nav a{color:var(--white);text-decoration:none;font-size:8.6px;font-weight:700;display:flex;align-items:center;padding:0 9px;border-right:1px solid rgba(255,255,255,.25)}
.search{position:absolute;left:567px;top:8px;width:111px;height:20px;background:var(--blue-dark);border:1px solid #3c8dd4;color:var(--white);font-size:8px;font-style:italic;font-weight:700;padding:4px 5px}

.hero{height:293px;position:relative;background:linear-gradient(100deg,#3a3a35 0%,#d8c74a 22%,#c9c9c4 40%,#5b5b55 60%,#a23c34 80%,#6b6a66 100%)}
.hero-caption{position:absolute;left:32px;top:194px;width:262px;height:77px;background:rgba(0,0,0,.6);padding:9px 14px}
.hero-caption h1{font-size:21px;font-weight:400;color:var(--yellow);line-height:1.2;margin-bottom:4px}
.hero-caption p{color:#eee;font-size:9.3px;line-height:1.3}

.intro{height:170px;display:flex;padding:20px 32px 0}
.intro-col{width:330px}
.intro h2{font-size:12.5px;color:var(--blue);font-weight:400;margin-bottom:8px}
.intro p{margin-bottom:10px}
.checklist{list-style:none;margin-top:2px}
.checklist li{display:flex;align-items:center;gap:9px;margin-bottom:4px}

.featured{height:211px;background:var(--dark);padding:20px 40px 0}
.featured h2{font-size:9.5px;color:var(--yellow);font-weight:400;margin-bottom:21px}
.project-grid{display:flex;justify-content:space-between;width:645px}
.project{width:151px}
.project-photo{height:85px;border:1px solid #999;margin-bottom:8px}
.project h3{font-size:9.6px;color:var(--white);font-weight:700}
.project p{color:#ddd;font-size:8.2px;line-height:1.5}

.testimonials{height:113px;padding:23px 0 0 86px}
.testimonial-box{width:536px;border-top:1px solid var(--line);border-bottom:1px solid var(--line);padding:8px 0 9px}
.testimonial-box h2{font-size:12.5px;color:var(--blue);font-weight:700;margin-bottom:2px}
.testimonial-box blockquote{font-style:italic;font-size:7.6px;line-height:1.75}
.testimonial-box cite{font-style:normal;color:#333;float:right;font-size:7.6px}

.site-footer{height:245px;background:var(--dark);display:flex;padding:25px 0 0 33px;font-family:"Ubuntu",sans-serif;color:#ccc}
.footer-col{font-size:7.6px;line-height:1.45}
.footer-col h3{font-size:11px;font-weight:400;color:#ddd;margin-bottom:19px}
.footer-col h3 strong{color:var(--white);font-weight:700}
.footer-col p{margin-bottom:17px;width:133px}
.footer-links{list-style:none;width:110px}
.footer-links li{font-size:7.6px;padding:2px 0 3px;border-bottom:1px solid #383838;text-transform:uppercase;color:#ddd}
.footer-links li:last-child{border-bottom:none}
.contact strong{color:var(--white);font-weight:500}
.stay{margin-top:16px;margin-left:6px}
.stay h3{margin-bottom:7px;padding-bottom:6px;border-bottom:1px solid #383838;width:110px}
.stay-icons{display:flex;gap:11px}
.stay-icons span{width:22px;height:22px;background:#eee;border-radius:3px}

.bottom-bar{height:64px;background:var(--darker);font-family:"Ubuntu",sans-serif;color:#ddd;text-align:center;font-size:7.6px;padding-top:12px;line-height:1.6}
.bottom-bar .legal{margin-top:8px}
.bottom-bar .legal strong{font-weight:500}
</style>
</head>
<body>
<div class="page">
  <header class="site-header">
    <div class="brand"><span class="brand-mark"></span><span class="brand-name">Korvanith Partners</span></div>
    <div class="social" aria-label="Social links"><span></span><span></span><span></span><span></span><span></span></div>
  </header>

  <nav class="main-nav">
    <a href="#">HOME</a><a href="#">PHILOSOPHY</a><a href="#">ACTIVITIES</a><a href="#">PROJECTS</a><a href="#">MANAGEMENT</a><a href="#">NEWS</a><a href="#">ABOUT</a><a href="#">CONTACT</a>
    <div class="search">Search here...</div>
  </nav>

  <section class="hero" role="img" aria-label="Photograph of a completed retail shopping strip with yellow and red shopfronts and shoppers on a sunny day">
    <div class="hero-caption">
      <h1>Halden, Australia</h1>
      <p>This is Draftwell's version of Lorem Ipsum. Proin gravida nibh vel velit auctor aliquet. Aenean sollicitudin.</p>
    </div>
  </section>

  <section class="intro">
    <div class="intro-col">
      <h2>ABOUT US</h2>
      <p>This is Draftwell's version of Lorem Ipsum. Proin gravida nibh vel velit auctor aliquet. Aenean sollicitudin, lorem quis bibendum auctor, nisi elit consequat ipsum, nec sagittis sem nibh id elit.</p>
      <p>Duis sed odio sit amet nibh vulputate cursus a sit amet mauris. Morbi accumsan ipsum velit. Nam nec tellus a odio tincidunt auctor a ornare odio. Sed non mauris vitae erat consequat auctor eu in elit. This is Draftwell's version of Lorem Ipsum. Proin gravida nibh vel velit auctor aliquet. Aenean sollicitudin, lorem quis bibendum auctor.</p>
    </div>
    <div class="intro-col">
      <h2>WHAT WE DO</h2>
      <p>This is Draftwell's version of Lorem Ipsum. Proin gravida nibh vel velit auctor aliquet. Aenean sollicitudin, lorem quis bibendum auctor,</p>
      <ul class="checklist">
        <li><svg width="16" height="10" viewBox="0 0 16 10"><path d="M0 0 L16 3 L12 10 Z" fill="#2f8fdd"/></svg>Nisi elit consequat ipsum</li>
        <li><svg width="16" height="10" viewBox="0 0 16 10"><path d="M0 0 L16 3 L12 10 Z" fill="#2f8fdd"/></svg>Nec sagittis sem nibh id elit.</li>
        <li><svg width="16" height="10" viewBox="0 0 16 10"><path d="M0 0 L16 3 L12 10 Z" fill="#2f8fdd"/></svg>Duis sed odio sit amet nibh vulputate cursus a sit amet mauris.</li>
        <li><svg width="16" height="10" viewBox="0 0 16 10"><path d="M0 0 L16 3 L12 10 Z" fill="#2f8fdd"/></svg>Morbi accumsan ipsum velit.</li>
      </ul>
    </div>
  </section>

  <section class="featured">
    <h2>FEATURED PROJECTS</h2>
    <div class="project-grid">
      <article class="project">
        <div class="project-photo" role="img" aria-label="Photograph of a retail centre with red shopfronts" style="background:linear-gradient(120deg,#7a9bbf,#c23b2e 55%,#8a8a86)"></div>
        <h3>PROIN GRAVIDA NIBH</h3>
        <p>Vel velit auctor aliquet. Aenean sollici-tudin, lorem quis bibendum auctor, nisi elit consequat ipsum.</p>
      </article>
      <article class="project">
        <div class="project-photo" role="img" aria-label="Aerial photograph of an industrial development under construction" style="background:linear-gradient(135deg,#5e7a45,#d9d9d4 50%,#6f6a5f)"></div>
        <h3>PROIN GRAVIDA NIBH</h3>
        <p>Vel velit auctor aliquet. Aenean sollici-tudin, lorem quis bibendum auctor, nisi elit consequat ipsum.</p>
      </article>
      <article class="project">
        <div class="project-photo" role="img" aria-label="Photograph of a retail store entrance with balloons" style="background:linear-gradient(180deg,#4c7fc7,#d1362b 45%,#8c8a84)"></div>
        <h3>PROIN GRAVIDA NIBH</h3>
        <p>Vel velit auctor aliquet. Aenean sollici-tudin, lorem quis bibendum auctor, nisi elit consequat ipsum.</p>
      </article>
      <article class="project">
        <div class="project-photo" role="img" aria-label="Photograph of a shopping centre opening day with a marquee" style="background:linear-gradient(120deg,#c8302a,#e9e6e0 50%,#b9322b)"></div>
        <h3>PROIN GRAVIDA NIBH</h3>
        <p>Vel velit auctor aliquet. Aenean sollici-tudin, lorem quis bibendum auctor, nisi elit consequat ipsum.</p>
      </article>
    </div>
  </section>

  <section class="testimonials">
    <div class="testimonial-box">
      <h2>TESTIMONIALS</h2>
      <blockquote>" This is Draftwell's version of Lorem Ipsum. Proin gravida nibh vel velit auctor aliquet. Aenean sollicitudin, lorem quis bibendum auctor, nisi elit conse-quat ipsum, nec sagittis sem nibh id elit. Duis sed odio sit amet nibh vulputate cursus a sit amet mauris" <cite>- Elsa Morvane, Australia</cite></blockquote>
    </div>
  </section>

  <footer class="site-footer">
    <div class="footer-col" style="width:150px">
      <h3><strong>ABOUT</strong> US</h3>
      <p>This is Draftwell's version of Lorem ipsum. Proin gravida nibh vel velit auctor aliquet. Aenean sollici-tudin, lorem quis bibendum auctor, nisi elit consequat ipsum.</p>
      <ul class="footer-links"><li>About us</li><li>What we do</li><li>Our services</li><li>News and events</li></ul>
    </div>
    <div class="footer-col" style="width:167px">
      <h3><strong>PRODUCTS /</strong> SERVICES</h3>
      <p>This is Draftwell's version of Lorem ipsum. Proin gravida nibh vel velit auctor aliquet. Aenean sollici-tudin.</p>
      <ul class="footer-links" style="margin-top:11px"><li>Featured</li><li>Specification</li><li>Poricing</li><li>Guarantee</li><li>Security</li></ul>
    </div>
    <div class="footer-col" style="width:179px">
      <h3><strong>EXTRA</strong> HEADINGS</h3>
      <p>This is Draftwell's version of Lorem ipsum. Proin gravida nibh vel velit auctor aliquet. Aenean sollici-tudin.roin gravida nibh vel velit auctor aliquet.</p>
      <ul class="footer-links"><li>Featured heading class 1</li><li>Featured heading second</li><li>Featured heading</li><li>Featured heading extra</li></ul>
    </div>
    <div class="footer-col contact" style="width:150px">
      <h3><strong>COMPANY</strong> INFOEADINGS</h3>
      <p><strong>Korvanith</strong><br>58 Harbour Reach Lane,<br>Marlow Bay</p>
      <p style="margin-top:-5px">Call us - 1800 6120 XXXX<br>Mail us - info@korvanith.com</p>
      <div class="stay">
        <h3><strong>STAY</strong> CONNECTED</h3>
        <div class="stay-icons"><span></span><span></span><span></span><span></span></div>
      </div>
    </div>
  </footer>

  <div class="bottom-bar">
    <p>This is Draftwell's version of Lorem Ipsum. Proin gravida nibh vel velit auctor aliquet. Aenean sollicitudin, lorem quis bibendum<br>auctor, nisi elit consequat ipsum, nec sagittis sem nibh id elit. Duis sed odio sit amet nibh vulputate cursus a sit amet mauris.</p>
    <p class="legal">© 2014 <strong>Korvanith LLC</strong> &nbsp;| &nbsp;All right reserved &nbsp;| &nbsp;Privacy policy</p>
  </div>
</div>
</body>
</html>
```